Brookvale Brochure & Fact Sheet

We need a brochure designed that we will distribute both digitally (PDF) and also have printed. We our an IT company and would like the creative to reflect our brand and industry. All content is written and ready to go. We need each page of the brochure provided as an individual file so we can arrange the pages as needed.

```html
<!DOCTYPE html>
<html lang="en">
<head>
<meta charset="utf-8">
<title>Brookvale Brochure</title>
<link rel="stylesheet" href="https://fonts.googleapis.com/css2?family=Montserrat:wght@500;600;700;800&family=Arimo:wght@400&display=swap">
<style>
  :root{
    --stage:#c9c6c4;
    --paper:#ffffff;
    --brand:#0a7bbd;
    --brand-deep:#075f93;
    --ink:#1d1d1b;
    --body:#2b2b2b;
    --panel-a:#0d8fc4;
    --panel-b:#0a4f78;
  }
  *{margin:0;padding:0;box-sizing:border-box}
  html,body{width:1200px;height:600px;overflow:hidden;background:var(--stage)}
  .stage{position:relative;width:1200px;height:600px}
  .page{position:absolute;top:59px;width:342px;height:483px;background:var(--paper);overflow:hidden}
  .page--cover{left:254px}
  .page--services{left:625px}
  .abs{position:absolute}

  .edge-tab{position:absolute;right:0;width:16px;background:var(--brand)}
  .brand-name{font-family:"Montserrat",sans-serif;font-weight:600;color:var(--ink);letter-spacing:-0.3px}

  /* cover */
  .cover-mark{left:226px;top:33px;display:flex;align-items:center;gap:4px;font-size:13px}
  .dot{width:11px;height:11px;border-radius:50%;background:var(--ink)}
  .cover-emblem{left:143px;top:213px}
  .rule{position:absolute;height:3px;background:var(--brand);left:0;width:46px;top:437px}
  .brand-square{position:absolute;left:46px;top:416px;width:43px;height:43px;background:var(--brand);border-radius:3px}
  .tagline{left:92px;top:417px;font-family:"Montserrat",sans-serif;color:var(--ink);line-height:1}
  .tagline__kicker{font-size:6.5px;font-weight:800;letter-spacing:.2px}
  .tagline__main{font-size:15.5px;font-weight:800;letter-spacing:-0.5px;line-height:.95;margin-top:1px}

  /* services */
  .page-title{right:26px;top:13px;text-align:right;font-family:"Montserrat",sans-serif;font-weight:800;font-size:19px;line-height:.92;color:var(--ink);letter-spacing:-0.6px}
  .heading{font-family:"Montserrat",sans-serif;font-weight:700;color:var(--brand);font-size:9.2px;line-height:1;letter-spacing:.1px}
  .copy{font-family:"Arimo",sans-serif;font-size:5.6px;line-height:1.22;color:var(--body);text-align:justify}
  .section{position:absolute;left:16px;width:137px}
  .section .heading{display:inline-block;border-bottom:1px solid var(--brand);padding-bottom:1px;margin-bottom:4px;padding-right:12px}
  .lead-bar{left:166px;top:64px;width:7px;height:92px;background:var(--brand)}
  .lead-heading{left:178px;top:64px;line-height:.98}
  .lead-copy{left:171px;top:97px;width:156px}
  .infra-head{left:171px;top:189px;width:156px;display:flex;align-items:center;gap:4px}
  .infra-head i{display:block;width:64px;height:1.5px;background:var(--brand)}
  .infra-copy{left:171px;top:200px;width:156px}
  .quote-panel{left:171px;top:280px;width:154px;height:186px}
  .quote-panel svg{position:absolute;inset:0}
  .quote-text{position:absolute;inset:0;display:flex;flex-direction:column;justify-content:center;text-align:center;font-family:"Montserrat",sans-serif;font-weight:600;color:#fff;font-size:7.6px;line-height:1.08;padding:0 10px}
  .quote-text p+p{margin-top:9px}
  .footer-mark{left:94px;top:429px;font-size:13px}
</style>
</head>
<body>
<div class="stage">

  <section class="page page--cover">
    <div class="edge-tab" style="top:16px;height:55px"></div>
    <div class="abs cover-mark"><span class="dot"></span><span class="brand-name">brookvale</span></div>
    <svg class="abs cover-emblem" width="56" height="56" viewBox="0 0 56 56" aria-hidden="true"><circle cx="28" cy="28" r="28" fill="var(--brand)"/></svg>
    <div class="rule"></div>
    <div class="brand-square"></div>
    <div class="abs tagline">
      <div class="tagline__kicker">BE A LEADER</div>
      <div class="tagline__main">ALIGN YOUR<br>TECHNOLOGY</div>
    </div>
  </section>

  <section class="page page--services">
    <div class="edge-tab" style="top:0;height:55px"></div>
    <h1 class="abs page-title">BROOKVALE<br>SERVICES</h1>

    <div class="abs lead-bar"></div>
    <h2 class="abs heading lead-heading">BROOKVALE<br>MANAGED<br>IT&nbsp;&nbsp;SERVICES</h2>
    <p class="abs copy lead-copy">Managed Services by Brookvale delivers proactive monitoring, maintenance, security and IT support for small and medium size business infrastructures, applications and cloud solutions. Based in Lake County, we provide a hands-on service approach and design end-to-end IT solutions that help your company grow efficiently, remain flexible, and maintain a lean IT operation. We employ a dedicated team of infrastructure experts that ensure your business operations are running smoothly, with no downtime, 24 hours a day. IT shouldn't be a disruption, but a reliable tool, and it's our job to make that happen</p>

    <div class="abs infra-head"><i></i><h2 class="heading">INFRASTRUCTURE</h2></div>
    <p class="abs copy infra-copy">We specialize in first architecting a streamlined IT system that works harmoniously and increases workflow efficiency. We then manage, monitor, and maintain all business networks and servers either on your premise or remotely. We provide 24-hour advanced network monitoring to all Managed Services partners; this allows us to proactively respond to alerts, avoid downtime, identify bottlenecks and manage security vulnerabilities. When it comes to IT, we stay on top of things – so you don't have to.</p>

    <div class="section" style="top:134px">
      <h2 class="heading">SECURITY</h2>
      <p class="copy">Our security services include endpoint security, network security, cloud security and policy management. We focus on protecting our partners from today's sophisticated cyber security threats by helping them outline, implement and maintain customized security policies and procedures. We stay abreast of all security developments and threats and strive to educate everyone on how to protect themselves both personally and professionally.</p>
    </div>
    <div class="section" style="top:218px">
      <h2 class="heading">DISASTER RECOVERY</h2>
      <p class="copy">No matter how well protected you are, it's better to plan for the unexpected. Brookvale collaborates with partners to plan, provide and manage disaster recovery solutions specific to their IT needs. Our disaster recovery plan includes off-site backups, complex disaster recovery solutions, and redundancy solutions. Be proactive and get your plan B in order with Brookvale.</p>
    </div>
    <div class="section" style="top:293px">
      <h2 class="heading">DESKTOP MANAGEMENT</h2>
      <p class="copy">We help your employees focus on the day-to-day business at hand by setting up efficient workstations, consistently keeping systems up-to-date, and fielding support questions 24/7. Count on reliable and secured workspaces from Brookvale.</p>
    </div>
    <div class="section" style="top:347px">
      <h2 class="heading">DESKTOP MANAGEMENT</h2>
      <p class="copy">Valuable business data needs to be stored and protected. We help businesses determine the best model for their needs, whether it's in the cloud, hosted on-site, or a hybrid of the two, and assist them with implementation, monitoring and maintenance.</p>
    </div>

    <div class="abs quote-panel">
      <svg width="154" height="186" viewBox="0 0 154 186" role="img" aria-label="Blue digital backdrop of flowing binary code">
        <defs>
          <radialGradient id="panelGlow" cx="35%" cy="45%" r="80%">
            <stop offset="0" stop-color="var(--panel-a)"/>
            <stop offset="1" stop-color="var(--panel-b)"/>
          </radialGradient>
        </defs>
        <rect width="154" height="186" fill="url(#panelGlow)"/>
      </svg>
      <div class="quote-text">
        <p>Customer service<br>is at the core of our<br>Brookvale team</p>
        <p>“ Our Managed IT Services<br>is successful<br>because we have a dedicated<br>and experienced team<br>ensuring your staff<br>receives rapid responses<br>and expert support<br>from technicians<br>they know and trust.”</p>
      </div>
    </div>

    <div class="rule"></div>
    <div class="brand-square"></div>
    <div class="abs footer-mark brand-name">brookvale</div>
  </section>

</div>
</body>
</html>
```